Webdesign für visa-korvenet.org
Kreativer Initialvorschlag, schnelle Umsetzung, flexible Anpassung des Designvorschlags und nette Kommunikation, gerne wieder!
Zielgruppe
Wir vermitteln weltweit Reisegenehmigungen für Geschäfts- und Privatkunden. Auf VISA-Korvenet.org möchten wir auf deutsch, englisch & chinesisch Reisenden bei der Beiholung von Kurzzeit, Work & Travel & diversen Visaarten helfen.
Aufgabenstellung
Der Webseitezweck ist es, dass Besucher bestellen. Dafür muss die Seite attraktiv, einfach bedienbar und das CTA Element "zum Formular" präsent und mehrfach auftauchen.

```html
<!DOCTYPE html>
<html lang="de">
<head>
<meta charset="utf-8">
<title>VISA Korvenet – eVisitor Visum Australien</title>
<link rel="stylesheet" href="https://fonts.googleapis.com/css2?family=Roboto:wght@300;400;500&display=swap">
<style>
:root{
  --navy:#0d3a78;
  --navy-text:#123f7d;
  --red:#b3121b;
  --page:#f4f4f4;
  --card:#ffffff;
  --text:#8a8a8a;
  --heading:#3a3a3a;
  --line:#e3e3e3;
  --footer:#ececec;
  --chip:#eef1f5;
}
*{box-sizing:border-box;margin:0;padding:0}
html,body{width:674px;height:1200px;overflow:hidden}
body{background:var(--page);font-family:'Roboto',sans-serif;font-weight:300;color:var(--text);position:relative}
.abs{position:absolute}
/* header */
.brand{left:137px;top:9px;display:flex;align-items:center;gap:4px}
.brand-mark{width:14px;height:14px;background:var(--navy);border-radius:50%}
.brand-name{font-size:7.5px;font-weight:500;color:var(--navy)}
.brand-tag{font-size:3px;color:var(--navy);display:block;margin-top:1px}
.contact{top:14px;font-size:7.4px;font-weight:500;color:var(--navy-text);display:flex;align-items:center;gap:4px}
.contact svg{width:7px;height:7px}
.phone{left:387px}
.hours{left:473px}
/* nav */
.nav{left:137px;top:37px;width:400px;height:17px;background:var(--navy);display:flex;align-items:center;font-size:5.6px;font-weight:400;color:#fff}
.nav span{position:absolute}
/* hero */
.hero{left:137px;top:61px;width:400px;height:148px;background:linear-gradient(180deg,#6aa8e8 0%,#9cc3e6 40%,#5e7f8e 58%,#2e5d88 75%,#1f4c78 100%)}
.hero-title{position:absolute;left:0;right:0;top:53px;text-align:center;font-size:15.5px;font-weight:400;color:#fff;text-shadow:0 1px 2px rgba(0,0,0,.55)}
.btn-red{position:absolute;left:161px;top:77px;width:77px;height:15px;background:var(--red);color:#fff;font-size:6px;font-weight:400;display:flex;align-items:center;justify-content:center}
.dots{position:absolute;left:194px;top:138px;display:flex;gap:3px}
.dots i{width:4.5px;height:4.5px;border-radius:50%;background:#fff}
.dots i+i{background:#b8c4d0}
/* cards */
.card{background:var(--card);box-shadow:0 0 2px rgba(0,0,0,.12);padding:0 5px}
.card-title{font-size:11px;font-weight:300;color:var(--navy-text);text-align:center}
.item-head{display:flex;align-items:center;gap:8px;font-size:6.4px;font-weight:400;color:var(--heading)}
.icon{width:14px;height:14px;flex:none;margin-left:2px}
p,li{font-size:5.4px;line-height:7px;letter-spacing:-.04px}
ul{list-style:none}
b{font-weight:500;color:#333}
h3{font-size:6.5px;font-weight:400;color:var(--heading);margin:9px 0 4px}
.divider{height:1px;background:var(--line);margin:7px 0}
.btn-outline{width:70px;height:15.5px;margin:10px auto 0;border:1px solid var(--navy);color:var(--navy-text);font-size:6.2px;font-weight:400;display:flex;align-items:center;justify-content:center}
.box1{left:137px;top:216px;width:288px;height:182px;padding-top:9px}
.box2{left:137px;top:405px;width:288px;height:107px;padding-top:10px}
.box3{left:137px;top:519px;width:288px;height:314px;padding-top:3px}
.box4{left:137px;top:841px;width:288px;height:260px;padding:5px 7px 0}
/* sidebar */
.pay{left:432px;top:216px;width:105px;height:64px;padding-top:8px}
.cards{display:flex;justify-content:center;gap:3px;margin-top:6px}
.paycard{width:22px;height:14px;border-radius:1.5px;background:var(--chip);border:1px solid #d6dce4;font-size:4px;font-weight:400;color:var(--navy-text);display:flex;align-items:center;justify-content:center}
.side{left:432px;top:287px;width:105px;height:261px;padding:8px 7px}
.side p{margin-bottom:7px;font-size:5.4px;line-height:6.8px}
.side a{color:var(--navy-text);text-decoration:none}
/* table */
table{width:274px;border-collapse:collapse;margin-top:7px;table-layout:fixed}
th,td{border:1px solid var(--line);text-align:left;font-size:5.5px;padding:0 7px;color:#555;font-weight:300}
th{font-size:6.2px;height:15.5px;white-space:nowrap}
th.h{padding:0 5px}
td{height:13.7px}
tr.two td{height:20.7px;line-height:7px}
td.c{text-align:center;padding:0}
td.c svg{width:6px;height:6px}
/* footer */
.footer{left:0;top:1118px;width:674px;height:82px;background:var(--footer)}
.fcol{position:absolute;top:23px;font-size:5.5px;line-height:6.8px}
.fcol h4{font-size:6.5px;font-weight:400;color:var(--navy-text);margin-bottom:3px}
.frule{position:absolute;left:142px;top:60px;width:390px;height:1px;background:#dcdcdc}
.copy{position:absolute;left:142px;top:67px;font-size:5.5px}
.legal{position:absolute;top:67px;font-size:5.5px;color:var(--navy-text)}
</style>
</head>
<body>
<svg width="0" height="0" style="position:absolute">
  <symbol id="tick" viewBox="0 0 10 10"><path d="M1.5 5.5 L4 8 L8.8 1.5" fill="none" stroke="#123f7d" stroke-width="1.8"/></symbol>
</svg>

<header>
  <div class="abs brand"><span class="brand-mark"></span><div><span class="brand-name">VISA Korvenet</span><span class="brand-tag">deutsches Formular - Visum Australien</span></div></div>
  <div class="abs contact phone"><svg viewBox="0 0 10 10"><path d="M2 1 L4 1 L4.6 3.4 L3.3 4.3 C4 5.8 4.5 6.3 5.8 6.9 L6.7 5.6 L9 6.2 L9 8.3 C5 8.8 1.4 5.2 2 1Z" fill="#b3121b"/></svg>0800 5550 1926</div>
  <div class="abs contact hours"><svg viewBox="0 0 10 10"><circle cx="5" cy="5" r="4" fill="none" stroke="#b3121b" stroke-width="1.2"/><path d="M5 2.6 V5 H7" fill="none" stroke="#b3121b" stroke-width="1"/></svg>Mo-Fr 10-16 Uhr</div>
</header>

<nav class="abs nav">
  <span style="left:29px">STARTSEITE</span>
  <span style="left:90px">TOURISTEN VISUM</span>
  <span style="left:168px">BUSINESS VISUM</span>
  <span style="left:243px">WAS IST ETA</span>
  <span style="left:306px">AGB</span>
  <span style="left:346px">KONTAKT</span>
</nav>

<section class="abs hero" role="img" aria-label="Foto: Hafen von Sydney mit Opernhaus und Skyline">
  <div class="hero-title">EVISITOR VISUM AUSTRALIEN</div>
  <div class="btn-red">REGISTRIEREN</div>
  <div class="dots"><i></i><i></i></div>
</section>

<section class="abs card box1">
  <div class="card-title">Unterscheidung</div>
  <div class="item-head" style="margin-top:6px"><svg class="icon" viewBox="0 0 14 14"><path d="M6.5 13 C7 9 7 6 6.5 4" fill="none" stroke="#0d3a78" stroke-width="1.3"/><path d="M6.5 4 C4 2 2 3 1.5 5 M6.5 4 C9 2 11.5 3 12 5 M6.5 4 C6 2 7 1 8.5 1" fill="none" stroke="#0d3a78" stroke-width="1.3"/></svg>eVisitor „Tourist ETA“ mit 12 Monaten Gültigkeit</div>
  <p style="margin-top:4px">Mit dem Visitor Visum können Touristen bis zu drei Monaten am Stück nach Australien reisen um dort Urlaub zu machen, Verwandte oder Bekannte zu besuchen. Eine arbeitsbezogene Nutzung dieses Visums ist ausdrücklich <b>nicht</b> gestattet!<br>Wichtig: Es muss bereits vor Antritt der Reise ein gültiges Visum vorliegen. Drucken Sie Ihre eVisitor Nummer aus und legen Sie diese Ihren Reisedokumenten bei.</p>
  <div class="divider"></div>
  <div class="item-head"><svg class="icon" viewBox="0 0 14 14"><circle cx="6" cy="6" r="5" fill="none" stroke="#0d3a78" stroke-width="1.2"/><path d="M1 6 H11 M6 1 C3.5 4 3.5 8 6 11 M6 1 C8.5 4 8.5 8 6 11" fill="none" stroke="#0d3a78" stroke-width=".8"/><circle cx="10" cy="9" r="2" fill="#0d3a78"/><path d="M6.8 13.5 C7 11.5 13 11.5 13.2 13.5Z" fill="#0d3a78"/></svg>eVisitor „Business ETA“ mit 12 Monaten Gültigkeit</div>
  <p style="margin-top:4px">Geschäftsreisende benötigen ein Business eVisitor Visum. Dieses ebenso elektronisch erstellte Visum hat eine Gültigkeit von 12 Monaten und kann für einen durchgängigen Geschäftsaufenthalt für bis zu drei Monaten genutzt werden. Wir empfehlen auch bei Messebesuchen ein Business Visum zu beantragen um eine problemlose Einreise zu gewährleisten.<br>Wichtig: Es muss bereits vor Antritt der Reise ein gültiges Business Visum vorliegen. Drucken Sie Ihre eVisitor Nummer aus und legen Sie diese Ihren Reisedokumenten bei.</p>
  <span class="btn-outline">REGISTRIEREN</span>
</section>

<aside class="abs card pay">
  <div class="card-title" style="line-height:12.5px">Zugelassene<br>Zahlungsmittel</div>
  <div class="cards"><span class="paycard">Nordpay</span><span class="paycard">Kelvo</span><span class="paycard">Tarix</span></div>
</aside>

<aside class="abs card side">
  <p>VISA-Korvenet.org ist ein nicht staatlicher Servicedienstleister für die Beantragung von Evisitor-Genehmigungen.</p>
  <p>Bei uns erhalten Sie die Evisitor-Einreisegenehmigung einschließlich unserer Serviceleistung. Jeder Antrag wird von einem deutschsprachigen Support Mitarbeiter geprüft und bearbeitet. Damit Sie ohne Probleme, z.B. Formfehler, nach Australien einreisen können.</p>
  <p>Sofern Sie den Antrag über uns anfordern, ist dieser 12 Monate ab Ausstellung gültig, es sein denn Ihr Reisepass läuft vorher ab.</p>
  <p>Sollten Sie die Evisitor Registrierungsnummer verlieren, so können Sie diese 12 Monate kostenfrei bei uns erneut in Ihrem Archiv abrufen. Neben dieser stehen Ihnen weitere Serviceleistungen zur Verfügung, diese Serviceleistung kostet 39 Euro und enthält alle anfallenden Gebühren.</p>
  <p>Sie können auch auf eigenes Risiko auf <a>https://www.visa-amt.au</a> Ihren Antrag stellen. Beachten Sie aber, dass Sie dann keine Unterstützung eines Live Supportmitarbeiters haben und die Gefahr besteht, fehlerhafte Eingaben zu tätigen.</p>
</aside>

<section class="abs card box2">
  <div class="item-head"><svg class="icon" viewBox="0 0 14 14"><rect x="2.5" y="0.5" width="9" height="13" rx="1" fill="#0d3a78"/><circle cx="7" cy="5" r="2.6" fill="none" stroke="#fff" stroke-width=".8"/><path d="M4.4 5 H9.6 M7 2.4 V7.6" stroke="#fff" stroke-width=".6"/><rect x="4.5" y="10" width="5" height="1.2" fill="#fff"/></svg>Welche Dokumente erhalte ich mit meinem Evisitor Visum?</div>
  <p style="margin-top:6px">Sobald Ihre Evisitor Genehmigung erteilt worden ist erhalten Sie eine Bestätigung per Email. Dieses Dokument müssen Sie aufheben und mit Ihren Reisedokumenten zur Reise mitnehmen. Die Evisitor Dokumente umfassen</p>
  <ul style="margin-top:7px"><li>• Ihre eVisitor Genehmigungsnummer</li><li>• Das Datum ab dem Ihre eVisitor Nummer gültig ist</li><li>• Die allgemeinen eVisitor Konditionen und Bedingungen</li></ul>
  <p style="margin-top:7px">Mit einer gültigen eVisitornummer (ETA Visum) erhalten Sie bei der Einreise nach Australien keinen Eintrag, bzw. Stempel mehr in Ihren Reisepass. Die Crew Ihrer Airline übermittelt bereits während des Fluges Ihre Pass und eVisitor Daten an die Australischen Behörden.</p>
</section>

<section class="abs card box3">
  <h3>Wann erhalte ich meine Evisitor ETA VISA Genehmigung?</h3>
  <p>Beide Evisitor Visa werden in der Regel umgehend gewährt, jedoch kann es in Ausnahmefällen zu einer Bearbeitungszeit von 2-10 Werktagen kommen. In äußerst seltenen Fällen kann eine Verweigerung einer Evisitor Genehmigung für die Einreise nach Australien auftreten. Diese wird jedoch schriftlich von den Australischen Behörden begründet. In diesem Fall empfehlen wir direkte Kontaktaufnahme mit der Australischen Botschaft in Berlin.</p>
  <h3>Was darf man als eVisitor (Inhaber eines ETA Visum) in Australien machen?</h3>
  <p>Als Tourist oder Geschäftsreisender dürfen Sie für den maximalen Zeitraum von drei Monaten ungehindert Australien bereisen. Die Evisitor Genehmigung gilt für ein Jahr, somit können wiederholte Reisen innerhalb dieses Zeitraums nach Australien unternommen werden. Die Australischen Behörden lassen darüber hinaus zu, dass eVisitor mit einem Touristen ETA Visum ehrenamtliche Tätigkeiten aufnehmen, solange diese ausschließlich unbezahlt (außer Essen, Nachtlager und geringfügiges Taschengeld) stattfinden und keinen vollbezahlten Arbeitsplatz eines australischen Staatsangehörigen gefährden oder gar ersetzten.<br>Australien gilt als liberales Land solange die Gesetze eingehalten werden. Unerlaubte Arbeiten, die Aufnahme von Studien oder Trainings darf nicht gegen Geld erfolgen und nicht länger wie drei Monate stattfinden.</p>
  <h3>3 Tipps für eine erfolgreiche Australien Reise</h3>
  <p>Gültige Reisedokumente für die gesamte Dauer des Aufenthaltes. Reisepass und vorläufiger Reisepass werden anerkannt. Kinder benötigen einen eigenen Reisepass. Personalausweis und vorläufiger Personalausweis sind nicht zugelassen Sollten Sie asiatische Staaten im Zuge der Reise besucht werden wollen, informieren Sie sich bitte über die speziellen Vorschriften, da manche Staaten eine Gültigkeit bis zu sechs Monaten ausländischer Reisepässe voraussetzen.</p>
  <p style="margin-top:7px">Australien hat sehr strikte Einreise und Quarantänevorschriften. An etlichen Flughäfen ist mit Körperscannern bei der Einreise zu rechnen. Ebenso müssen eingeführte Nahrungsmittel, Tier- und Pflanzenprodukte auf der Einreisekarte angegeben werden. Striktes Befolgen der Anweisungen wird von uns empfohlen um unnötige Wartezeiten und Ärger zu vermeiden.</p>
  <p style="margin-top:7px">Halten Sie sich an die Gesetze des Landes. Wie bereits erwähnt ist Australien ein liberales Land, solange die Gesetze befolgt werden. Illegale Aktivitäten wie Verstöße gegen die Visa Bestimmungen, die Ausfuhr von kulturellen Schätzen oder die Einnahme von illegalen Substanzen können zur Ausweisung bis hin zu Freiheitstrafe in Australien führen.</p>
  <h3>Welche Staaten können Evisitor für Australien in Anspruch nehmen?</h3>
  <p>Andorra, Belgien, Brunei, Dänemark, <b>Deutschland</b>, Finnland, Frankreich, Griechenland, Großbritannien, Hong Kong, Irland, Island, Italien, Japan, Kanada, Liechtenstein, Luxemburg, Malaysia, Malta, Monaco, Niederlande, Nordirland, Norwegen, Österreich, Portugal, San Marino, Schweden, Schweiz, Singapur, Spanien, Südkorea, USA, Vatikan</p>
</section>

<section class="abs card box4">
  <div class="card-title">Ihre Vorteile mit www.visa-korvenet.org in der Übersicht</div>
  <table>
    <colgroup><col style="width:147.6px"><col style="width:62.8px"><col style="width:62.8px"></colgroup>
    <tr><th>Unser Service</th><th class="h">visa-korvenet.org</th><th class="h">visa-amt.au</th></tr>
    <tr><td>Anmeldeformular auf deutsch</td><td class="c"><svg><use href="#tick"/></svg></td><td></td></tr>
    <tr><td>Hilfe bei der Formulareingabe</td><td class="c"><svg><use href="#tick"/></svg></td><td></td></tr>
    <tr><td>Email Support</td><td class="c"><svg><use href="#tick"/></svg></td><td></td></tr>
    <tr><td>Auf Wunsch auch Sendung der ETA Nummer per Post</td><td class="c"><svg><use href="#tick"/></svg></td><td></td></tr>
    <tr><td>FAQ Section</td><td class="c"><svg><use href="#tick"/></svg></td><td class="c"><svg><use href="#tick"/></svg></td></tr>
    <tr><td>Kontrolle Ihrer gemachten Eingaben</td><td class="c"><svg><use href="#tick"/></svg></td><td class="c"><svg><use href="#tick"/></svg></td></tr>
    <tr class="two"><td>Rückmeldung und Überprüfung ob Ihre Eingaben<br>abgeschickt wurden</td><td class="c"><svg><use href="#tick"/></svg></td><td class="c"><svg><use href="#tick"/></svg></td></tr>
    <tr class="two"><td>Manuelle Kontrolle bei Falscheingaben und<br>Rückmeldung durch Supportmitarbeiter</td><td class="c"><svg><use href="#tick"/></svg></td><td></td></tr>
    <tr><td>Statusnachricht Ihres ETA-Antrages</td><td class="c"><svg><use href="#tick"/></svg></td><td></td></tr>
    <tr><td>ETA-Nummer Versand bequem per PDF</td><td class="c"><svg><use href="#tick"/></svg></td><td></td></tr>
    <tr><td>Aufbewahrung Ihrer ETA Nummer für ein Jahr</td><td class="c"><svg><use href="#tick"/></svg></td><td class="c"><svg><use href="#tick"/></svg></td></tr>
    <tr class="two"><td>Kostenlose Neuanforderung Ihrer ETA Nummer<br>innerhalb eines Jahres bei Verlust</td><td class="c"><svg><use href="#tick"/></svg></td><td class="c"><svg><use href="#tick"/></svg></td></tr>
    <tr class="two"><td>Garantierte Rückerstattung der Gebührenkosten, falls<br>Ihre ETA Genehmigung zurückgewiesen wird</td><td class="c"><svg><use href="#tick"/></svg></td><td></td></tr>
  </table>
</section>

<footer class="abs footer">
  <div class="fcol" style="left:142px"><h4>Informationen</h4>Gültigkeitsdauer ETA Visum</div>
  <div class="fcol" style="left:310px"><h4>Quicklinks</h4>ETA Formular deutsch<br>Was ist ETA</div>
  <div class="fcol" style="left:460px"><h4>Bearbeitungszeiten</h4>MO-DO 09.00 Uhr - 17.30 Uhr<br>FR 09.00 Uhr - 16.00 Uhr</div>
  <div class="frule"></div>
  <div class="copy">© 2017 VISA Korvenet</div>
  <div class="legal" style="left:442px">Datenschutz</div>
  <div class="legal" style="left:483px">AGB</div>
  <div class="legal" style="left:503px">Impressum</div>
</footer>
</body>
</html>
```